Carpentry Fitouts business Van half wrap

We are looking for a half wrap on our 2020Mitsubishi Express van.
Template attached, base colour to be white

Van colour is white. The 2 blue colours from logo plus black should be used in the half wrap

Our services are :
Commercial Carpentry
Interior Fitouts
Plastering
Suspended Ceilings
Windows & Doors

Rear window to have perforated one way film

Contact details on van should be PH:0412 905 638
dale@keelstonebuilds.com.au

Industry/Entity Type

Carpentry Fitouts

Colors
0054AA
0677BA
7BADD7
CADEEF
E8F1F8
0094D4
00A9DD
6FCCEA
C7EBF8
E9F6FB

Requirements
Nice to have
• Wrap not through door handles

```html
<!DOCTYPE html>
<html lang="en">
<head>
<meta charset="utf-8">
<title>Keelstone Builds – Van Half Wrap</title>
<link href="https://fonts.googleapis.com/css2?family=League+Gothic&family=Poppins:wght@500;700&family=Roboto+Condensed:wght@700&display=swap" rel="stylesheet">
<style>
  :root{
    --canvas:#ffffff;
    --van-white:#f1f3f5;
    --van-edge:#d7dbe0;
    --navy:#262a63;
    --teal:#1aa6cc;
    --teal-deep:#0f7fa3;
    --charcoal:#1d2121;
    --text-light:#ffffff;
  }
  *{margin:0;padding:0;box-sizing:border-box}
  html,body{width:1200px;height:1200px;overflow:hidden;background:var(--canvas)}
  .sheet{position:relative;width:1200px;height:1200px}
  .wrap-side{position:absolute;left:0;width:1200px;height:560px}
  .wrap-side--navy{top:0;--panel-dark:var(--navy);--stripe-top:var(--teal);--stripe-base:var(--navy)}
  .wrap-side--black{top:562px;--panel-dark:var(--charcoal);--stripe-top:var(--navy);--stripe-base:var(--charcoal)}
  .body-panel{fill:var(--van-white);stroke:var(--van-edge);stroke-width:2}
  .rocker{fill:var(--charcoal)}
  .panel-dark{fill:var(--panel-dark)}
  .accent-teal{fill:var(--teal)}
  .accent-deep{fill:var(--teal-deep);opacity:.35}
  .stripe-top{fill:var(--stripe-top)}
  .stripe-base{fill:var(--stripe-base)}
  .emblem-circle{fill:var(--navy);stroke:var(--van-white);stroke-width:10}
  .brand-name{font-family:"League Gothic",sans-serif;font-size:62px;fill:var(--teal)}
  .services{font-family:"Roboto Condensed",sans-serif;font-weight:700;font-size:11.5px;fill:var(--text-light)}
  .services .dot{fill:var(--teal)}
  .phone{font-family:"Poppins",sans-serif;font-weight:700;font-size:25px;fill:var(--navy)}
  .web{font-family:"Poppins",sans-serif;font-weight:500;font-size:16px;fill:var(--teal)}
</style>
</head>
<body>
<main class="sheet">

  <svg class="wrap-side wrap-side--navy" viewBox="0 0 1200 560" aria-label="Van side wrap, navy version">
    <path class="body-panel" d="M75 481 L75 330 Q80 270 150 250 L230 225 Q300 170 360 130 Q380 115 420 115 L1080 115 Q1108 115 1110 150 L1110 481 Z"/>
    <path class="panel-dark" d="M835 115 L1080 115 Q1108 115 1110 150 L1110 440 L800 440 Z"/>
    <path class="accent-deep" d="M820 440 L870 350 L905 365 L880 440 Z"/>
    <path class="accent-teal" d="M1010 430 Q1050 370 1110 355 L1110 385 Q1060 392 1040 432 Z"/>
    <circle class="emblem-circle" cx="694" cy="281" r="138"/>
    <rect class="stripe-top" x="331" y="402" width="300" height="17"/>
    <rect class="stripe-base" x="319" y="431" width="791" height="34"/>
    <rect class="rocker" x="75" y="465" width="1035" height="16"/>
    <text class="brand-name" x="860" y="225" textLength="230" lengthAdjust="spacingAndGlyphs">KEELSTONE BUILDS</text>
    <text class="services" x="966" y="309" text-anchor="middle" textLength="206" lengthAdjust="spacingAndGlyphs">COMMERCIAL CARPENTRY <tspan class="dot">•</tspan> INTERIOR FITOUTS</text>
    <text class="services" x="966" y="325" text-anchor="middle">PLASTERING <tspan class="dot">•</tspan> SUSPENDED CEILINGS</text>
    <text class="services" x="966" y="340" text-anchor="middle">WINDOWS &amp; DOORS</text>
    <text class="phone" x="316" y="346" textLength="209" lengthAdjust="spacingAndGlyphs">0412 905 638</text>
    <text class="web" x="318" y="370" textLength="205" lengthAdjust="spacingAndGlyphs">keelstonebuilds.com.au</text>
  </svg>

  <svg class="wrap-side wrap-side--black" viewBox="0 0 1200 560" aria-label="Van side wrap, black version">
    <path class="body-panel" d="M75 481 L75 330 Q80 270 150 250 L230 225 Q300 170 360 130 Q380 115 420 115 L1080 115 Q1108 115 1110 150 L1110 481 Z"/>
    <path class="panel-dark" d="M835 115 L1080 115 Q1108 115 1110 150 L1110 440 L800 440 Z"/>
    <path class="accent-deep" d="M820 440 L870 350 L905 365 L880 440 Z"/>
    <path class="accent-teal" d="M1010 430 Q1050 370 1110 355 L1110 385 Q1060 392 1040 432 Z"/>
    <circle class="emblem-circle" cx="694" cy="281" r="138"/>
    <rect class="stripe-top" x="331" y="402" width="300" height="17"/>
    <rect class="stripe-base" x="319" y="431" width="791" height="34"/>
    <rect class="rocker" x="75" y="465" width="1035" height="16"/>
    <text class="brand-name" x="860" y="225" textLength="230" lengthAdjust="spacingAndGlyphs">KEELSTONE BUILDS</text>
    <text class="services" x="966" y="309" text-anchor="middle" textLength="206" lengthAdjust="spacingAndGlyphs">COMMERCIAL CARPENTRY <tspan class="dot">•</tspan> INTERIOR FITOUTS</text>
    <text class="services" x="966" y="325" text-anchor="middle">PLASTERING <tspan class="dot">•</tspan> SUSPENDED CEILINGS</text>
    <text class="services" x="966" y="340" text-anchor="middle">WINDOWS &amp; DOORS</text>
    <text class="phone" x="316" y="346" textLength="209" lengthAdjust="spacingAndGlyphs">0412 905 638</text>
    <text class="web" x="318" y="370" textLength="205" lengthAdjust="spacingAndGlyphs">keelstonebuilds.com.au</text>
  </svg>

</main>
</body>
</html>
```